Stationery design for law/Property/finance business

We need stationery design for a Law/Property/Finance business called Stonebridge. Logo is attached.
we require a letterhead and with compliments slip.
Would like to see a very simple professional design using the colours of the logo and offset against Charcoal colours. Maybe a charcoal band for header and footer with logo and details appearing in it? Former letterhead attached for examples.
we require the project to be provided in word, pdf and jpeg format.
we require the following details on the stationery:
Coralby Phone: 07 41592036
Westra Phone: 07 41357904
Mobile: 0427 915 384
Fax: 07 41836257
email: admin@stonebridgeholdings.com.au
ABN 52 304 781 619

```html
<!DOCTYPE html>
<html lang="en">
<head>
<meta charset="utf-8">
<title>Stonebridge Stationery – Letterhead and With Compliments Slip</title>
<link rel="stylesheet" href="https://fonts.googleapis.com/css2?family=Mulish:wght@400;600;800&family=PT+Sans:wght@400&family=Roboto+Condensed:wght@400&display=swap">
<style>
  :root {
    --backdrop: #8f8f8f;
    --charcoal: #1f1f1f;
    --paper: #ffffff;
    --brand-blue: #1a8ad4;
    --accent-blue: #35b2e6;
    --ink: #1b1b1b;
    --ink-light: #ffffff;
  }
  * { box-sizing: border-box; margin: 0; padding: 0; }
  html, body { width: 1200px; height: 1200px; overflow: hidden; }
  body {
    background: var(--backdrop);
    position: relative;
    font-family: "Mulish", Arial, sans-serif;
  }
  .sheet {
    position: absolute;
    background: var(--paper);
    box-shadow: 2px 3px 5px rgba(0,0,0,0.35);
    overflow: hidden;
  }
  .sheet__header {
    position: absolute;
    left: 0; top: 0; width: 100%;
    background: var(--charcoal);
  }
  .sheet__footer-band {
    position: absolute;
    left: 0; bottom: 0; width: 100%;
    background: var(--charcoal);
  }
  .footer-slash {
    position: absolute;
    top: -2px; bottom: -2px;
    width: 6px;
    background: var(--paper);
    transform: skewX(-45deg);
  }
  .brand {
    position: absolute;
    display: flex;
    align-items: center;
    gap: 7px;
    color: var(--brand-blue);
    font-weight: 800;
    letter-spacing: 0.02em;
    text-transform: uppercase;
  }
  .brand__dot {
    border-radius: 50%;
    background: var(--accent-blue);
  }
  .header-details {
    position: absolute;
    color: var(--ink-light);
    line-height: 1.3;
  }
  .header-details__email { display: flex; align-items: center; gap: 3px; }
  .icon { fill: currentColor; flex: none; }
  .contact-row {
    position: absolute;
    display: flex;
    align-items: center;
    font-family: "Roboto Condensed", "Arial Narrow", sans-serif;
    color: var(--ink);
    white-space: nowrap;
  }
  .contact-row__item { display: flex; align-items: center; gap: 3px; }
  .contact-row__place { margin-left: 3px; }

  /* Letterhead */
  .letterhead { left: 95px; top: 52px; width: 515px; height: 728px; }
  .letterhead .sheet__header { height: 67px; }
  .letterhead .brand { left: 64px; top: 20px; font-size: 19px; }
  .letterhead .brand__dot { width: 16px; height: 16px; }
  .letterhead .header-details { left: 326px; top: 34px; font-size: 8.4px; }
  .letterhead .contact-row { left: 52px; top: 700px; font-size: 6.6px; gap: 10px; }
  .letterhead .sheet__footer-band { height: 12px; }
  .letterhead .footer-slash { left: 377px; }

  /* Compliments slip */
  .comp-slip { left: 426px; top: 836px; width: 686px; height: 324px; }
  .comp-slip .sheet__header { height: 73px; }
  .comp-slip .brand { left: 50px; top: 23px; font-size: 20px; }
  .comp-slip .brand__dot { width: 17px; height: 17px; }
  .comp-slip .header-details { left: 449px; top: 31px; font-size: 11px; }
  .comp-slip__title {
    position: absolute;
    left: 41px; top: 252px;
    font-family: "PT Sans", Arial, sans-serif;
    font-weight: 400;
    font-size: 22px;
    color: var(--accent-blue);
  }
  .comp-slip .contact-row { left: 41px; top: 289px; font-size: 9.2px; gap: 13px; }
  .comp-slip .sheet__footer-band { height: 14px; }
  .comp-slip .footer-slash { left: 512px; width: 7px; }
</style>
</head>
<body>

<svg width="0" height="0" style="position:absolute" aria-hidden="true">
  <symbol id="icon-mail" viewBox="0 0 10 10"><path d="M1 4l4-3 4 3v5H1z M2 4.5l3 2 3-2" /></symbol>
  <symbol id="icon-mobile" viewBox="0 0 10 10"><path d="M3 0h4a1 1 0 0 1 1 1v8a1 1 0 0 1-1 1H3a1 1 0 0 1-1-1V1a1 1 0 0 1 1-1zm0 1.5v5.5h4V1.5z" /></symbol>
  <symbol id="icon-fax" viewBox="0 0 10 10"><path d="M3 1h4v3H3z M1 4h8v6H1z M0 4h1v6H0z" /></symbol>
  <symbol id="icon-phone" viewBox="0 0 12 10"><path d="M0 4c0-2 2-3 6-3s6 1 6 3v1H9V3.5H3V5H0z M2 6l2-2h4l2 2v3H2z" /></symbol>
</svg>

<section class="sheet letterhead" aria-label="Letterhead">
  <header class="sheet__header">
    <div class="brand"><span class="brand__dot"></span>Stonebridge</div>
    <div class="header-details">
      <div class="header-details__email"><svg class="icon" width="9" height="9"><use href="#icon-mail"/></svg>admin@stonebridgeholdings.com.au</div>
      <div>ABN 52 304 781 619</div>
    </div>
  </header>
  <div class="contact-row">
    <span class="contact-row__item"><svg class="icon" width="7" height="7"><use href="#icon-mobile"/></svg>0427 915 384</span>
    <span class="contact-row__item"><svg class="icon" width="7" height="7"><use href="#icon-fax"/></svg>07 41836257</span>
    <span class="contact-row__item"><svg class="icon" width="9" height="7"><use href="#icon-phone"/></svg>07 41592036<span class="contact-row__place">(Coralby)</span></span>
    <span class="contact-row__item"><svg class="icon" width="9" height="7"><use href="#icon-phone"/></svg>07 41357904<span class="contact-row__place">(Westra)</span></span>
  </div>
  <div class="sheet__footer-band"><span class="footer-slash"></span></div>
</section>

<section class="sheet comp-slip" aria-label="With compliments slip">
  <header class="sheet__header">
    <div class="brand"><span class="brand__dot"></span>Stonebridge</div>
    <div class="header-details">
      <div class="header-details__email"><svg class="icon" width="11" height="11"><use href="#icon-mail"/></svg>admin@stonebridgeholdings.com.au</div>
      <div>ABN 52 304 781 619</div>
    </div>
  </header>
  <h2 class="comp-slip__title">With Compliments</h2>
  <div class="contact-row">
    <span class="contact-row__item"><svg class="icon" width="10" height="10"><use href="#icon-mobile"/></svg>0427 915 384</span>
    <span class="contact-row__item"><svg class="icon" width="10" height="10"><use href="#icon-fax"/></svg>07 41836257</span>
    <span class="contact-row__item"><svg class="icon" width="12" height="9"><use href="#icon-phone"/></svg>07 41592036<span class="contact-row__place">(Coralby)</span></span>
    <span class="contact-row__item"><svg class="icon" width="12" height="9"><use href="#icon-phone"/></svg>07 41357904<span class="contact-row__place">(Westra)</span></span>
  </div>
  <div class="sheet__footer-band"><span class="footer-slash"></span></div>
</section>

</body>
</html>
```